IT-support company web-site design

We need to re-design out site for existing clients and for the future promotions. Site needs to be attractive with intuitive interface. We need to keep our logo and colors but any reshuffles can be made. I provide the working site and re-made version, which we do nt like. It has to be more bright and clear. All the blocks have to be divided and look like logic and structured. PLease find the addresses to work with below.
The "real" one https://plorim.com
The version http://dostuly.net/Plorim/
If you have any с

Industry/Entity Type

It Company

Number of Pages Required

5+ page

Font styles to use
Sans Serif

Colors
9bcb3c

Requirements
Must have
• Our LOGO and our colors (green palette). We d like to make our services blocks as the main things. We need to have our images and slogans as there are extremely important advantages of our company.
Nice to have
• Original and modern view of the site.
Should not have
• unpredictable and @surprising@, hard- definable buttons and ways

```html
<!DOCTYPE html>
<html lang="en">
<head>
<meta charset="utf-8">
<title>Plorim – IT Support</title>
<link href="https://fonts.googleapis.com/css2?family=Mulish:wght@300;400;600;700&display=swap" rel="stylesheet">
<style>
:root{
  --green:#9bcb3c;
  --green-dark:#7fb02a;
  --green-soft:#c9e59a;
  --ink:#3d3d3d;
  --text:#555;
  --muted:#888;
  --dark:#333a3a;
  --darker:#2b2f2f;
  --gray:#6a6a6a;
  --light:#f1f1f1;
  --white:#fff;
}
*{box-sizing:border-box;margin:0;padding:0}
html,body{width:1200px;height:4358px;overflow:hidden}
body{font-family:"Mulish",Arial,sans-serif;color:var(--text);background:var(--white);position:relative}
section,header,footer{position:relative;width:1200px;overflow:hidden}
.btn{display:inline-block;background:var(--green);color:var(--white);font-size:20px;text-transform:uppercase;text-align:center;letter-spacing:.5px}
.brand{display:flex;align-items:center;gap:14px;font-size:44px;font-weight:400;letter-spacing:1px}
.brand .dot{width:26px;height:26px;border-radius:50%;background:var(--green)}
.section-title{font-size:40px;font-weight:400;color:var(--green);text-align:center;display:flex;align-items:center;justify-content:center;gap:24px}
.section-title::before,.section-title::after{content:"";width:120px;height:2px;background:currentColor;opacity:.6}

/* header */
.site-header{height:107px;border-bottom:1px solid #e4e4e4}
.site-header .brand{position:absolute;left:80px;top:30px;color:var(--ink)}
.main-nav{position:absolute;right:70px;top:30px;display:flex;font-size:17px}
.main-nav a{padding:10px 18px;color:var(--green-dark);text-decoration:none}
.main-nav a.active{background:var(--green);color:var(--white)}
.search-icon{position:absolute;right:40px;top:38px}

/* hero */
.hero{height:576px}
.hero-photo{position:absolute;inset:0;background:linear-gradient(100deg,#6a6f6e 0%,#a9acaa 40%,#d8d9d6 70%,#bfc2bf 100%)}
.hero-box{position:absolute;left:80px;top:140px;width:545px;height:276px;background:rgba(60,60,60,.72);border:2px solid rgba(255,255,255,.55);text-align:center;color:var(--white)}
.hero-box h1{font-size:56px;font-weight:400;color:var(--green);margin-top:20px;letter-spacing:1px;white-space:nowrap}
.hero-box .line{font-size:40px;font-weight:300;line-height:1.05}
.hero-box .line2{font-size:30px;font-weight:300}
.hero-box .btn{margin-top:22px;padding:14px 34px}
.hero-dots{position:absolute;left:568px;top:520px;display:flex;gap:10px}
.hero-dots span{width:14px;height:14px;border-radius:50%;border:2px solid var(--white)}
.hero-dots span.on{background:var(--green);border-color:var(--green)}

/* quote strip */
.quote-strip{height:73px;background:linear-gradient(90deg,#5fb39a,#8dc56a 50%,#9bcb3c)}
.quote-strip p{position:absolute;left:80px;top:22px;color:var(--white);font-size:24px}
.quote-strip .quote-btn{position:absolute;right:130px;top:12px;width:212px;height:50px;background:var(--white);color:var(--green-dark);font-size:20px;line-height:50px;text-align:center}

/* about */
.about{height:421px}
.about h2{position:absolute;left:80px;top:50px;font-size:38px;font-weight:400;color:var(--ink)}
.about h2 span{color:var(--green)}
.about p{position:absolute;left:80px;top:108px;width:720px;font-size:15px;line-height:1.95}
.about .btn{position:absolute;left:80px;top:290px;width:206px;height:52px;line-height:52px}
.about-art{position:absolute;left:843px;top:85px;width:217px;height:292px;background:linear-gradient(160deg,#e9e9e9,#bdbdbd 60%,#f0a830)}

/* services */
.services{height:790px;color:var(--white)}
.services-bg{position:absolute;inset:0;background:linear-gradient(160deg,#4a4f4f,#2e3333 60%,#3f4545)}
.services .section-title{position:absolute;top:55px;width:100%;color:var(--green)}
.svc{position:absolute;font-size:14px;line-height:1.6;color:#e6e6e6}
.svc h3{font-size:24px;font-weight:400;color:var(--green);margin-bottom:2px}
.svc.center{width:330px;text-align:center}
.svc.left{width:270px}
.svc.left h3{text-align:right}
.svc.right{width:300px}
.hub{position:absolute;left:0;top:0}

/* advisers */
.advisers{height:581px}
.advisers h2{position:absolute;left:80px;top:48px;font-size:38px;font-weight:400;color:var(--green)}
.card{position:absolute;top:125px;width:292px;height:212px;padding:22px 24px;font-size:14px;line-height:1.75;color:var(--white)}
.card.green{background:var(--green)}
.card.grey{background:var(--gray)}
.card::after{content:"";position:absolute;left:40px;bottom:-20px;border:20px solid transparent;border-bottom:0}
.card.green::after{border-top-color:var(--green)}
.card.grey::after{border-top-color:var(--gray)}
.person{position:absolute;top:360px;display:flex;align-items:center;gap:18px}
.avatar{width:92px;height:92px;border-radius:50%;border:4px solid var(--green);background:linear-gradient(180deg,#d8d8d8,#8e8e8e)}
.person.grey .avatar{border-color:var(--gray)}
.person b{display:block;font-size:22px;font-weight:400;color:var(--green)}
.person.grey b{color:var(--gray)}
.person small{font-size:15px;color:var(--muted)}
.slider-dots{position:absolute;left:562px;top:502px;display:flex;gap:9px}
.slider-dots span{width:14px;height:14px;border-radius:50%;border:2px solid #bbb}
.slider-dots span.on{background:#bbb}

/* partners */
.partners{height:125px;background:var(--light);display:flex;align-items:center;justify-content:space-around;padding:0 40px}
.partners span{width:150px;height:62px;background:#d2d2d2;border-radius:4px}

/* banner */
.banner{height:262px;background:linear-gradient(110deg,#b5d974,#9bcb3c 45%,#8cbd31)}
.banner p{position:absolute;left:0;width:100%;top:90px;text-align:center;color:var(--white);font-size:33px;line-height:1.3}
.banner p b{font-weight:700;color:var(--ink)}

/* blog */
.blog{height:508px}
.blog .section-title{position:absolute;top:60px;width:100%}
.post{position:absolute;top:140px;width:250px}
.post .thumb{height:165px}
.post h4{margin-top:22px;font-size:23px;font-weight:400;line-height:1.15;color:var(--green)}
.post time{display:flex;align-items:center;gap:8px;margin-top:14px;font-size:13px;color:var(--muted)}

/* callback */
.callback{height:262px;background:#5d5d5d;color:var(--white)}
.callback h2{position:absolute;left:80px;top:45px;font-size:36px;font-weight:700;line-height:1.05}
.callback p{position:absolute;left:80px;top:128px;width:400px;font-size:14px;line-height:1.75;color:#e2e2e2}
.callback .ask{position:absolute;left:527px;top:48px;font-size:18px}
.field{position:absolute;height:48px;background:var(--white);color:var(--muted);font-size:14px;padding:14px 12px}
.send{position:absolute;left:830px;top:152px;width:168px;height:48px;background:var(--green);color:var(--white);text-align:center;line-height:48px;font-size:18px}

/* map */
.map{height:204px;background:linear-gradient(135deg,#dfe4d6,#cfd8c3 50%,#e6e8df)}

/* footer */
.site-footer{height:386px;background:var(--darker);color:#cfcfcf}
.site-footer .brand{position:absolute;left:125px;top:55px;color:var(--white);font-size:40px}
.about-f{position:absolute;left:115px;top:130px;width:245px;font-size:14px;line-height:1.75}
.socials{position:absolute;left:130px;top:290px;display:flex;gap:14px}
.socials span{width:48px;height:48px;border-radius:50%;border:2px solid #cfcfcf}
.f-col h5{font-size:17px;font-weight:400;color:var(--green);letter-spacing:1px;margin-bottom:18px}
.f-col{position:absolute;top:65px;font-size:13px}
.links li{list-style:none;margin-bottom:12px;display:flex;gap:12px;align-items:center}
.links li::before{content:"";width:8px;height:8px;border-radius:50%;background:var(--green)}
.contact-row{display:flex;gap:12px;margin-bottom:14px;line-height:1.5}
.contact-row svg{flex:none}
.news p{width:250px;line-height:1.7}
.news .email{margin-top:16px;width:250px;height:44px;background:var(--white);color:var(--muted);padding:13px 10px}
.news .sub{margin-top:14px;width:166px;height:44px;border-radius:22px;background:var(--green);color:var(--white);line-height:44px;text-align:center;font-size:16px}
.bottom-bar{height:63px;background:var(--green);color:var(--white);text-align:center;line-height:63px;font-size:13px}
</style>
</head>
<body>

<header class="site-header">
  <div class="brand"><span class="dot"></span>Plorim</div>
  <nav class="main-nav">
    <a class="active">Home</a><a>Plorim Difference</a><a>Services</a><a>Resources</a><a>Customers</a><a>Support</a><a>Contact us</a>
  </nav>
  <svg class="search-icon" width="22" height="22" viewBox="0 0 22 22"><circle cx="9" cy="9" r="7" fill="none" stroke="#999" stroke-width="2"/><line x1="14" y1="14" x2="20" y2="20" stroke="#999" stroke-width="2"/></svg>
</header>

<section class="hero">
  <div class="hero-photo" role="img" aria-label="Photo of a smiling help desk agent wearing a headset in an office"></div>
  <div class="hero-box">
    <h1>PLORIM PROVIDES</h1>
    <div class="line">LIVE LOCAL 24/7</div>
    <div class="line2">HELP DESK AND TIER # SUPPORT</div>
    <span class="btn">Contact us</span>
  </div>
  <div class="hero-dots"><span></span><span class="on"></span><span></span></div>
</section>

<section class="quote-strip">
  <p>Looking For Best It Services with Plorim?</p>
  <div class="quote-btn">Get a Quote &nbsp;›</div>
</section>

<section class="about">
  <h2>About <span>Plorim</span></h2>
  <p>Lorem Ipsum is simply dummy text of the printing and typesetting industry. Lorem Ipsum has been the industry's standard dummy text ever since the 1500s, when an unknown printer took a galley of type and scrambled it to make a type specimen book. It has survived not only five centuries, but also the leap into electronic typesetting, remaining essentially unchanged. It was popularised in the 1960s with the release of Letraset sheets containing Lorem Ipsum passages, and more recently with desktop publishing software like Aldus PageMaker including versions of Lorem Ipsum.</p>
  <span class="btn">Contact us</span>
  <div class="about-art" role="img" aria-label="Illustration of a businessman giving a thumbs up on a rising row of blocks"></div>
</section>

<section class="services">
  <div class="services-bg" role="img" aria-label="Dark photo of a team working at laptops"></div>
  <h2 class="section-title">Plorim Services</h2>

  <svg class="hub" width="1200" height="790" viewBox="0 0 1200 790">
    <circle cx="601" cy="425" r="160" fill="none" stroke="#9bcb3c" stroke-width="3" opacity=".22"/>
    <circle cx="601" cy="425" r="94" fill="#9bcb3c" opacity=".35"/>
    <circle cx="601" cy="425" r="80" fill="#fff" stroke="#9bcb3c" stroke-width="8"/>
    <circle cx="601" cy="425" r="64" fill="none" stroke="#9bcb3c" stroke-width="2"/>
    <text x="601" y="433" text-anchor="middle" font-family="Mulish, sans-serif" font-size="24" fill="#9bcb3c">Plorim</text>
    <g fill="#fff" stroke="#9bcb3c" stroke-width="6">
      <circle cx="601" cy="285" r="52"/>
      <circle cx="462" cy="365" r="52"/>
      <circle cx="740" cy="365" r="52"/>
      <circle cx="462" cy="505" r="52"/>
      <circle cx="740" cy="505" r="52"/>
      <circle cx="601" cy="585" r="52"/>
    </g>
    <g fill="none" stroke="#444" stroke-width="3" stroke-linecap="round" stroke-linejoin="round">
      <path d="M588 276 l13-13 13 13 M601 263 v22"/><path d="M614 295 l-13 13 -13-13 M601 308 v-22"/>
      <rect x="447" y="345" width="30" height="40" rx="3"/><path d="M468 355 q-6-4-12 0 q-4 6 6 9 q8 3 4 9 q-6 4-12 0 M462 350 v30"/>
      <circle cx="740" cy="353" r="9"/><path d="M722 387 q18-24 36 0"/>
      <path d="M444 507 v-6 a18 18 0 0 1 36 0 v6"/><rect x="440" y="503" width="8" height="14" rx="3"/><rect x="476" y="503" width="8" height="14" rx="3"/>
      <circle cx="740" cy="493" r="7"/><circle cx="726" cy="499" r="5"/><circle cx="754" cy="499" r="5"/><path d="M728 521 q12-18 24 0"/>
      <path d="M601 563 l18 7 v14 q0 14-18 22 q-18-8-18-22 v-14z"/><path d="M593 585 l6 6 10-11"/>
    </g>
  </svg>

  <div class="svc center" style="left:436px;top:130px"><h3>Approach</h3>Lorem Ipsum is simply dummy text of the printing and typesetting industry.</div>
  <div class="svc left" style="left:116px;top:318px"><h3>Relative Cost</h3>Lorem Ipsum is simply dummy text of the printing and typesetting industry...(+)</div>
  <div class="svc right" style="left:816px;top:318px"><h3>RISK</h3>Lorem Ipsum is simply dummy text of the printing and typesetting industry...(+)</div>
  <div class="svc left" style="left:116px;top:458px"><h3>Support</h3>Lorem Ipsum is simply dummy text of the printing and typesetting industry...(+)</div>
  <div class="svc right" style="left:816px;top:458px"><h3>Resources</h3>Lorem Ipsum is simply dummy text of the printing and typesetting industry...(+)</div>
  <div class="svc center" style="left:436px;top:654px"><h3>Reliability</h3>Lorem Ipsum is simply dummy text of the printing and typesetting industry.</div>
</section>

<section class="advisers">
  <h2>Plorim Adviser</h2>
  <div class="card green" style="left:80px">"Lorem Ipsum is simply dummy text of the printing and typesetting industry. Lorem Ipsum has been the industry's standard dummy text ever since the 1500s, when an unknown printer took a galley of type and specimen book"</div>
  <div class="card grey" style="left:455px">"Lorem Ipsum is simply dummy text of the printing and typesetting industry. Lorem Ipsum has been the industry's standard dummy text ever since the 1500s, when an unknown printer took a galley of type and specimen book"</div>
  <div class="card grey" style="left:832px">"Lorem Ipsum is simply dummy text of the printing and typesetting industry. Lorem Ipsum has been the industry's standard dummy text ever since the 1500s, when an unknown printer took a galley of type and specimen book"</div>
  <div class="person" style="left:80px"><div class="avatar" role="img" aria-label="Portrait photo of the manager"></div><div><b>Rona Velt</b><small>Manager</small></div></div>
  <div class="person grey" style="left:455px"><div class="avatar" role="img" aria-label="Portrait photo of the designer"></div><div><b>Rona Velt</b><small>Designer</small></div></div>
  <div class="person grey" style="left:832px"><div class="avatar" role="img" aria-label="Portrait photo of the founder"></div><div><b>Rona Velt</b><small>Founder</small></div></div>
  <div class="slider-dots"><span></span><span class="on"></span><span></span><span></span></div>
</section>

<section class="partners" aria-label="Partner badges">
  <span></span><span></span><span></span><span></span><span></span><span></span>
</section>

<section class="banner">
  <p>To help <b>PLORIM</b> Provides best Services and their act<br>together before they talk to investors.</p>
</section>

<section class="blog">
  <h2 class="section-title">Latest Blog</h2>
  <article class="post" style="left:78px"><div class="thumb" role="img" aria-label="Photo of a support agent with a headset" style="background:linear-gradient(135deg,#d9dde0,#8a9aa8)"></div><h4>Lorem Ipsum is simply dummy the typesetting.</h4><time><svg width="14" height="14" viewBox="0 0 14 14"><rect x="1" y="2" width="12" height="11" fill="none" stroke="#999"/><line x1="1" y1="5" x2="13" y2="5" stroke="#999"/></svg>8 October 2017</time></article>
  <article class="post" style="left:343px"><div class="thumb" role="img" aria-label="Photo of a business team meeting" style="background:linear-gradient(135deg,#c9b59b,#6e5a48)"></div><h4>Lorem Ipsum is simply dummy the typesetting.</h4><time><svg width="14" height="14" viewBox="0 0 14 14"><rect x="1" y="2" width="12" height="11" fill="none" stroke="#999"/><line x1="1" y1="5" x2="13" y2="5" stroke="#999"/></svg>8 October 2017</time></article>
  <article class="post" style="left:608px"><div class="thumb" role="img" aria-label="Photo of colleagues around a table" style="background:linear-gradient(135deg,#e4dccf,#9c8c78)"></div><h4>Lorem Ipsum is simply dummy the typesetting.</h4><time><svg width="14" height="14" viewBox="0 0 14 14"><rect x="1" y="2" width="12" height="11" fill="none" stroke="#999"/><line x1="1" y1="5" x2="13" y2="5" stroke="#999"/></svg>8 October 2017</time></article>
  <article class="post" style="left:872px"><div class="thumb" role="img" aria-label="Photo of a presenter with charts on a wall" style="background:linear-gradient(135deg,#eceeee,#a5abad)"></div><h4>Lorem Ipsum is simply dummy the typesetting.</h4><time><svg width="14" height="14" viewBox="0 0 14 14"><rect x="1" y="2" width="12" height="11" fill="none" stroke="#999"/><line x1="1" y1="5" x2="13" y2="5" stroke="#999"/></svg>8 October 2017</time></article>
</section>

<section class="callback">
  <h2>Request a Call<br>Back.</h2>
  <p>Lorem Ipsum is simply dummy text of the printing and typesetting industry. Lorem Ipsum has been the industry's standard dummy text ever since the 1500s.</p>
  <div class="ask">I would like to talk about...</div>
  <div class="field" style="left:527px;top:95px;width:290px">Name*</div>
  <div class="field" style="left:830px;top:95px;width:292px">Email*</div>
  <div class="field" style="left:527px;top:152px;width:290px">Phone No*</div>
  <div class="send">SEND</div>
</section>

<section class="map" role="img" aria-label="Street map showing the office location with a pin"></section>

<footer class="site-footer">
  <div class="brand"><span class="dot"></span>Plorim</div>
  <p class="about-f">Lorem Ipsum is simply dummy text of the printing and typesetting industry Lorem Ipsum.Lorem Ipsum has been the</p>
  <div class="socials"><span></span><span></span><span></span></div>

  <div class="f-col" style="left:418px">
    <h5>USEFUL LINK</h5>
    <ul class="links"><li>Home</li><li>Plorim Difference</li><li>Services</li><li>Customers</li><li>Support</li><li>Contact</li></ul>
  </div>

  <div class="f-col" style="left:620px">
    <h5>CONTACT US</h5>
    <div class="contact-row"><svg width="16" height="20" viewBox="0 0 16 20"><path d="M8 19 C2 11 1 9 1 7 a7 7 0 0 1 14 0 c0 2-1 4-7 12z" fill="#9bcb3c"/><circle cx="8" cy="7" r="2.5" fill="#2b2f2f"/></svg><div><b style="color:#9bcb3c;font-weight:400">PLORIM</b><br>4820 Larkfield Avenue,<br>Brenmoor, TX 77190</div></div>
    <div class="contact-row"><svg width="16" height="16" viewBox="0 0 16 16"><path d="M3 1 l3 3 -2 2 q2 4 6 6 l2-2 3 3 -2 2 q-8 0-12-12z" fill="#9bcb3c"/></svg>(555) - 310 - 7284</div>
    <div class="contact-row"><svg width="16" height="14" viewBox="0 0 16 14"><rect x="1" y="1" width="14" height="12" fill="#9bcb3c"/><path d="M1 1 l7 6 7-6" stroke="#2b2f2f" fill="none"/></svg>info@plorim.com</div>
    <div class="contact-row"><svg width="16" height="16" viewBox="0 0 16 16"><circle cx="8" cy="8" r="7" fill="#9bcb3c"/></svg>www.dostuly.net</div>
  </div>

  <div class="f-col news" style="left:872px">
    <h5>NEWSLETTER</h5>
    <p>Would you like to receive exclusive access to articles, white papers and our regular monthly newsletter?</p>
    <div class="email">Enter Email Id</div>
    <div class="sub">SUBSCRIBE</div>
  </div>
</footer>

<div class="bottom-bar">Copyright 2017 Plorim | All Rights Reserved</div>

</body>
</html>
```